Menu Design Project

Hi! I am looking for a menu design for a company opening up in Downtown Dallas. The company's name is Marbury Bakes and the colors are Tiffany Blue and Brown. The company is a cupcake factory and the vibe we are going for is a cupcake/coffee shop where people can come in, relax and still be able to work on work stuff etc. Think wood, glass and stainless steel. Very modern and professional. We would love for the menu to be kept simple, not too complicated and perhaps try to keep it at 1 double sided sheet of paper. The ones we have currently at a store are 4X6, but 5X7 sounds good too.
Updates

Hi!

We would like to have two different size options, 4X6 and 5X7. We want a menu that is portable, that customers can take with them and that we can include in their carry-out bags. We want it to be double sided to maximize the space. I have also uploaded an example of what we are looking for, feel free to use those names in your menu and prices, we might change them afterwards.Thanks,

Industry/Entity Type

Store

Requirements
Must have
• Must be Tiffany Blue and Brown. Must have the store's logo on there (attached), map for location, information about facebook page, and mobile app. We are going to have about 27 different cupcake flavors but we will also be making cakepops, cakes and beverages (lattes, cappuccinos, frappes, smoothies, coffee, hot cocoa, etc).

Store Address: 2917 Quill Ave, Dallas TX 75431

Store Hours:
Mon-Thur 10am-9pm
Fri-Sat 10am-10pm
Sun 12pm-7pm

Phone number: 2145831097

website: www.marburybakes-demo.com
Nice to have
• Would love for it to be double sided.

```html
<!DOCTYPE html>
<html lang="en">
<head>
<meta charset="utf-8">
<title>Marbury Bakes – Menu Card 6x4</title>
<link rel="stylesheet" href="https://fonts.googleapis.com/css2?family=Questrial&family=Roboto:wght@400;700&family=Roboto+Condensed:wght@400;700&family=Kaushan+Script&display=swap">
<style>
  :root {
    --tiffany: #5fc4cc;
    --tiffany-pale: #d9eff2;
    --tiffany-band: #c6e6eb;
    --brown: #4a2a1c;
    --ink: #555555;
    --ink-strong: #3a3a3a;
    --paper: #ffffff;
    --map-base: #e9e6df;
  }
  * { box-sizing: border-box; margin: 0; padding: 0; }
  html, body { width: 1200px; height: 880px; overflow: hidden; background: var(--paper); }
  .canvas { position: relative; width: 1200px; height: 880px; }
  .menu-card {
    position: absolute; left: 120px; top: 120px; width: 960px; height: 640px;
    background: var(--paper); border: 1px solid #dcdcdc; overflow: hidden;
    font-family: "Questrial", sans-serif; color: var(--ink);
  }
  .header-band { position: absolute; left: 0; top: 0; width: 960px; height: 110px; }
  .brand {
    position: absolute; left: 0; width: 960px; top: 80px; text-align: center;
    font-family: "Questrial", sans-serif; font-size: 38px; line-height: 44px; color: var(--tiffany);
    letter-spacing: 0.5px;
  }
  .menu-column { position: absolute; top: 146px; }
  .menu-column.hot { left: 39px; }
  .menu-column.cold { left: 267px; }
  .menu-heading {
    font-family: "Questrial", sans-serif; font-weight: 400; font-size: 25px;
    color: var(--tiffany); margin-bottom: 6px; line-height: 30px;
  }
  .menu-list { list-style: none; font-size: 17px; line-height: 20px; color: var(--ink); }
  .menu-list li { height: 20px; white-space: nowrap; }
  .menu-list .price { font-family: "Roboto", sans-serif; font-weight: 700; color: var(--ink-strong); line-height: 0; }
  .corporate-tag { position: absolute; left: 425px; top: 295px; width: 210px; height: 135px; }
  .corporate-tag .tag-text {
    position: absolute; left: 0; top: 28px; width: 210px; text-align: center;
    font-family: "Kaushan Script", cursive; font-size: 21px; line-height: 25px; color: var(--brown);
    transform: rotate(12deg);
  }
  .app-row { position: absolute; left: 41px; top: 458px; width: 575px; }
  .app-icons { position: absolute; left: 0; top: -12px; display: flex; gap: 6px; align-items: flex-end; }
  .app-icons span { display: block; width: 26px; height: 30px; border-radius: 5px; }
  .app-icons .ios { background: #8e8e8e; border-radius: 50%; width: 26px; height: 26px; }
  .app-icons .android { background: #8bbb2f; }
  .app-icons .web { background: #e8582a; }
  .app-text {
    font-style: italic; font-size: 17px; line-height: 21px; color: var(--ink-strong);
    text-indent: 108px;
  }
  .app-text strong { font-family: "Roboto", sans-serif; font-weight: 700; }
  .website-pill {
    position: absolute; left: 37px; top: 567px; width: 370px; height: 34px; border-radius: 17px;
    background: var(--tiffany); color: var(--paper); text-align: center;
    font-family: "Roboto", sans-serif; font-weight: 700; font-size: 24px; line-height: 34px;
  }
  .hours {
    position: absolute; right: 335px; top: 530px; text-align: right;
    font-family: "Roboto Condensed", sans-serif; font-size: 21px; line-height: 23px; color: var(--brown);
  }
  .hours strong { font-weight: 700; }
  .column-rule { position: absolute; left: 636px; top: 158px; width: 1.5px; height: 441px; background: var(--brown); }
  .location { position: absolute; left: 659px; top: 153px; width: 268px; font-family: "Roboto Condensed", sans-serif; color: var(--tiffany); }
  .location .intro { font-size: 15.5px; line-height: 19px; }
  .location .address { font-family: "Roboto", sans-serif; font-weight: 700; font-size: 17px; line-height: 21px; margin-top: 9px; font-style: normal; }
  .location .phone { font-family: "Roboto", sans-serif; font-weight: 700; font-size: 23px; line-height: 28px; margin-top: 7px; letter-spacing: 1.2px; white-space: nowrap; }
  .location .directions { font-size: 14.5px; line-height: 19px; margin-top: 9px; }
  .map-area {
    position: absolute; left: 663px; top: 415px; width: 259px; height: 182px;
    background: linear-gradient(135deg, var(--map-base) 0%, #efe7b8 45%, var(--map-base) 100%);
  }
</style>
</head>
<body>
<div class="canvas">
  <article class="menu-card">
    <svg class="header-band" viewBox="0 0 960 110" aria-hidden="true">
      <path d="M0 0 H960 V88 C880 86 780 90 700 84 C640 78 600 50 540 42 C470 34 400 42 330 56 C240 72 120 84 0 86 Z" fill="var(--tiffany-band)"/>
      <path d="M0 86 C120 84 240 72 330 56 C400 42 470 34 540 42 C600 50 640 78 700 84 C780 90 880 86 960 88" fill="none" stroke="var(--brown)" stroke-width="5"/>
      <path d="M0 94 C120 92 240 80 330 64 C400 50 470 42 540 50 C600 58 640 86 700 92 C780 98 880 94 960 96" fill="none" stroke="var(--brown)" stroke-width="1.5"/>
    </svg>
    <div class="brand">Marbury Bakes</div>

    <section class="menu-column hot">
      <h2 class="menu-heading">hot beverages</h2>
      <ul class="menu-list">
        <li>coffee <span class="price">3</span></li>
        <li>espresso shot <span class="price">3</span></li>
        <li>cafe latte <span class="price">3</span></li>
        <li>vanilla latte <span class="price">3</span></li>
        <li>caramel macciato <span class="price">3</span></li>
        <li>cafe mocha <span class="price">3</span></li>
        <li>cappucino <span class="price">3</span></li>
        <li>americano <span class="price">3</span></li>
        <li>chai tea latte <span class="price">3</span></li>
        <li>tea <span class="price">3</span></li>
        <li>hot chocolate <span class="price">3</span></li>
      </ul>
    </section>

    <section class="menu-column cold">
      <h2 class="menu-heading">cold beverages</h2>
      <ul class="menu-list">
        <li>frozen caramel latte <span class="price">3</span></li>
        <li>frozen mocha <span class="price">3</span></li>
        <li>very berry smoothie <span class="price">3</span></li>
        <li>strawberry banana smoothie <span class="price">3</span></li>
        <li>sweet tea <span class="price">3</span></li>
        <li>bottled water <span class="price">3</span></li>
        <li>bottled drinks <span class="price">3</span></li>
      </ul>
    </section>

    <div class="corporate-tag">
      <svg width="210" height="135" viewBox="0 0 210 135" aria-hidden="true">
        <path d="M22 8 C60 2 100 14 150 18 C175 20 195 30 200 46 L204 108 C206 124 196 130 180 128 C140 122 90 110 40 112 C20 113 8 106 6 90 L4 28 C4 16 10 10 22 8 Z"
              fill="var(--tiffany-pale)" stroke="var(--tiffany)" stroke-width="2"/>
      </svg>
      <p class="tag-text">Ask us about our<br>corporate prices<br>&amp; special!</p>
    </div>

    <div class="app-row">
      <div class="app-icons" aria-hidden="true">
        <span class="ios"></span><span class="android"></span><span class="web"></span>
      </div>
      <p class="app-text">Download our <strong>FREE</strong> Mobile App to get exclusive deals, sales notifications &amp; more! You can skip the line &amp; order through our Mobile App!</p>
    </div>

    <div class="website-pill">www.marburybakes-demo.com</div>

    <div class="hours">
      HOURS:<br>
      Mon-Thur <strong>10-9</strong><br>
      Fri-Sat <strong>10-10</strong>&nbsp; Sun <strong>12-7</strong>
    </div>

    <div class="column-rule"></div>

    <aside class="location">
      <p class="intro">We are located in Downtown Dallas, where Quill Ave meets Harlow St.</p>
      <address class="address">2917 Quill Ave<br>Dallas TX 75431</address>
      <p class="phone">Ph: (214) 583.1097</p>
      <p class="directions">If you are travelling North East on Northgate Freeway, take the exit towards Corwin St &amp; merge onto N. Corwin St, turn left on to Bellamy St &amp; take the 2nd right onto Harlow St. Take a right onto Quill Ave, we are on the left.</p>
    </aside>

    <div class="map-area" role="img" aria-label="Street map of downtown showing the bakery location at Quill Ave and Harlow St"></div>
  </article>
</div>
</body>
</html>
```